Hydroponic Farm Needs a Business Card

We need a business card design for a hydroponic farm located on the Gulf Coast called 'Tallowbend Farms'. We grow many forms of lettuce and tomatoes along with other herbs and spices. We currently sell to farmer's markets though will soon be expanding to commercial accounts such as restaurants and grocery stores. The colors should be bright and vibrant to reflect the nature of our produce. The final design should communicate a professional, clean, yet friendly impression and able to be used both with farmer's markets and commercial accounts.

The pictures are an example of our product. The pictures do not have to be incorporated into the business card design.

Please put areas for information such as Names, Phone Number, E-mail address, and additional information.

Industry/Entity Type

Farm

```html
<!DOCTYPE html>
<html lang="en">
<head>
<meta charset="utf-8">
<title>Tallowbend Farms – Business Card</title>
<link href="https://fonts.googleapis.com/css2?family=Montserrat:wght@700&family=Josefin+Sans:wght@300;400&display=swap" rel="stylesheet">
<style>
  :root {
    --backdrop: #8c9097;
    --card: #232323;
    --pink: #f08cb0;
    --rule: #bdbdbd;
    --light: #e6e6e6;
  }
  html, body {
    margin: 0;
    width: 1200px;
    height: 901px;
    overflow: hidden;
    background: var(--backdrop);
  }
  .sheet {
    width: 1200px;
    height: 901px;
    display: flex;
    flex-direction: column;
    align-items: center;
    justify-content: center;
    gap: 40px;
  }
  .card {
    position: relative;
    width: 700px;
    height: 400px;
    background: var(--card);
    box-shadow: 0 8px 22px rgba(0,0,0,.35);
    overflow: hidden;
  }
  .card-accents {
    position: absolute;
    inset: 0;
  }
  .card-accents polygon { fill: var(--pink); }

  /* Front */
  .front-lockup {
    position: absolute;
    left: 0; right: 0;
    top: 140px;
    text-align: center;
  }
  .brand-name {
    font-family: "Montserrat", sans-serif;
    font-weight: 700;
    color: var(--pink);
    font-size: 46px;
    letter-spacing: 1px;
    margin: 0;
    line-height: 1;
  }
  .slogan-row {
    display: flex;
    align-items: center;
    justify-content: center;
    gap: 14px;
    margin-top: 14px;
  }
  .rule {
    height: 1px;
    background: var(--rule);
  }
  .rule.long { width: 150px; }
  .rule.short { width: 60px; }
  .slogan {
    font-family: "Josefin Sans", sans-serif;
    font-weight: 400;
    color: var(--light);
    font-size: 17px;
    letter-spacing: 3px;
  }
  .ornament {
    display: block;
    margin: 8px auto 0;
    background: linear-gradient(90deg, transparent, #6e6e6e, transparent);
    border-radius: 3px;
  }
  .front-lockup .ornament { width: 90px; height: 8px; }

  /* Back */
  .back-details {
    position: absolute;
    left: 70px;
    top: 70px;
    width: 360px;
    text-align: center;
  }
  .back-brand {
    display: flex;
    align-items: center;
    justify-content: center;
    gap: 12px;
  }
  .brand-dot {
    width: 22px;
    height: 22px;
    border-radius: 50%;
    background: var(--pink);
  }
  .back-brand .brand-name { font-size: 30px; }
  .position {
    font-family: "Josefin Sans", sans-serif;
    font-weight: 300;
    color: var(--light);
    font-size: 15px;
    letter-spacing: 4px;
    margin-top: 8px;
  }
  .back-details .ornament { width: 120px; height: 22px; margin-top: 10px; }
  .back-details .rule { width: 340px; margin: 6px auto 0; }
  .contact {
    list-style: none;
    padding: 0;
    margin: 14px 0 0;
    font-family: "Josefin Sans", sans-serif;
    font-weight: 400;
    color: var(--pink);
    font-size: 19px;
    line-height: 1.3;
  }
  .address {
    font-family: "Josefin Sans", sans-serif;
    font-weight: 300;
    color: var(--light);
    font-size: 16px;
    letter-spacing: 5px;
    margin-top: 10px;
    padding-top: 8px;
    border-top: 1px solid #777;
    display: inline-block;
  }
</style>
</head>
<body>
<main class="sheet">

  <section class="card card-front" aria-label="Card front">
    <svg class="card-accents" viewBox="0 0 700 400" aria-hidden="true">
      <polygon points="20,95 175,30 30,70"/>
      <polygon points="520,30 690,20 690,55"/>
      <polygon points="560,380 690,260 690,300"/>
      <polygon points="20,380 220,355 40,395"/>
    </svg>
    <div class="front-lockup">
      <h1 class="brand-name">TALLOWBEND FARMS</h1>
      <div class="slogan-row">
        <span class="rule long"></span>
        <span class="slogan">YOUR SLOGAN</span>
        <span class="rule long"></span>
      </div>
      <span class="ornament" role="img" aria-label="Decorative flourish"></span>
    </div>
  </section>

  <section class="card card-back" aria-label="Card back">
    <svg class="card-accents" viewBox="0 0 700 400" aria-hidden="true">
      <polygon points="560,20 690,15 690,50"/>
      <polygon points="540,370 690,240 690,280"/>
      <polygon points="470,385 600,355 480,395"/>
    </svg>
    <div class="back-details">
      <div class="back-brand">
        <span class="brand-dot"></span>
        <h2 class="brand-name">TALLOWBEND FARMS</h2>
      </div>
      <div class="position">OFFICIAL POSITION</div>
      <span class="ornament" role="img" aria-label="Decorative flourish"></span>
      <div class="rule"></div>
      <ul class="contact">
        <li>+1234-5678-9000</li>
        <li>www.social/name.com</li>
        <li>youremail@website.com</li>
      </ul>
      <div class="address">YOUR ADDRESS</div>
    </div>
  </section>

</main>
</body>
</html>
```